Have Logo - Need Business Card Design!!!

I am looking for a business card design for a real estate development business. The company name is Orvane Realty Partners. I already have a logo created by Pixel Harbor and would like this logo to be incorporated into the design. I have uploaded the files. The card needs to be professional, but visually interesting. Not necessary to be double-sided, but if you want to get creative and can think of something to put on the back then have at it.

Target Market(s)

The target audience for these business cards will be professionals in the real estate industry.

Industry/Entity Type

Real Estate

Requirements
Must have
• The business card must have all the necessary items for a business card, i.e. company name, our logo, name (however, not title necessary), office address, office phone number, cell number, fax number, website address, etc.

You can use the information below for the card:

Martin R. Oswell
812 Linden Avenue
San Francisco, California 94177

www.orvanerealtypartners.example
moswell@orvanerealtypartners.example
Office: 415-555-0143
Fax: 415-555-0147
Cell: 415-555-0182

```html
<!DOCTYPE html>
<html lang="en">
<head>
<meta charset="utf-8">
<title>Orvane Realty Partners – Business Card</title>
<link rel="stylesheet" href="https://fonts.googleapis.com/css2?family=Tinos:wght@400&display=swap">
<style>
  :root {
    --green: #1f8a3b;
    --green-deep: #39a72a;
    --green-light: #7ec66c;
    --navy: #243a73;
    --ink: #1a1a1a;
    --paper: #ffffff;
    --edge: #bdbdbd;
  }
  * { margin: 0; padding: 0; box-sizing: border-box; }
  html, body {
    width: 1200px; height: 951px; overflow: hidden;
    background: var(--paper);
    font-family: "Tinos", "Times New Roman", serif;
  }
  .canvas { position: relative; width: 1200px; height: 951px; }

  .card-front {
    position: absolute; left: 42px; top: 55px;
    width: 727px; height: 407px;
    background: radial-gradient(ellipse at 50% 45%, var(--green-light) 0%, #5db84c 55%, var(--green-deep) 100%);
    display: flex; align-items: center; justify-content: center;
  }
  .brand { display: flex; align-items: center; gap: 14px; }
  .brand-mark { width: 22px; height: 22px; }
  .brand-name { font-weight: 400; letter-spacing: 0.02em; white-space: nowrap; }
  .card-front .brand-mark { background: var(--paper); }
  .card-front .brand-name { color: var(--paper); font-size: 52px; }

  .card-back {
    position: absolute; left: 438px; top: 484px;
    width: 727px; height: 406px;
    background: var(--paper);
    border: 1px solid var(--edge);
  }
  .card-back .brand {
    position: absolute; top: 40px; left: 0; right: 0; justify-content: center; gap: 10px;
  }
  .card-back .brand-mark { width: 14px; height: 14px; background: var(--navy); }
  .card-back .brand-name { color: var(--green); font-size: 30px; }

  .person-name {
    position: absolute; top: 134px; left: 0; right: 0; text-align: center;
    color: var(--green); font-size: 30px;
  }
  .address {
    position: absolute; top: 180px; left: 266px;
    font-size: 15.5px; line-height: 21px; color: var(--ink);
  }
  .label { color: var(--green); }
  .contact-web {
    position: absolute; top: 268px; left: 24px;
    font-size: 15.5px; line-height: 22px; color: var(--ink);
  }
  .contact-phone {
    position: absolute; top: 268px; right: 26px; text-align: right;
    font-size: 15.5px; line-height: 22px; color: var(--ink);
  }
  .stripe {
    position: absolute; left: 0; right: 0; top: 379px; height: 11px;
    display: flex;
  }
  .stripe-green { width: 369px; background: var(--green); }
  .stripe-navy { flex: 1; background: var(--navy); }
</style>
</head>
<body>
<main class="canvas">
  <section class="card-front" aria-label="Card front">
    <div class="brand">
      <span class="brand-mark"></span>
      <span class="brand-name">Orvane Realty Partners</span>
    </div>
  </section>

  <section class="card-back" aria-label="Card back">
    <div class="brand">
      <span class="brand-mark"></span>
      <span class="brand-name">Orvane Realty Partners</span>
    </div>
    <h1 class="person-name" style="font-weight:400">Martin R. Oswell</h1>
    <p class="address">
      <span class="label">Address:</span> 812 Linden Avenue<br>
      San Francisco, California 94177
    </p>
    <p class="contact-web">
      <span class="label">E-mail:</span> moswell@orvanerealtypartners.example<br>
      <span class="label">Website:</span> www.orvanerealtypartners.example
    </p>
    <p class="contact-phone">
      <span class="label">Office:</span> 415-555-0143<br>
      <span class="label">Fax:</span> 415-555-0147<br>
      <span class="label">Cell:</span> 415-555-0182
    </p>
    <div class="stripe"><span class="stripe-green"></span><span class="stripe-navy"></span></div>
  </section>
</main>
</body>
</html>
```